Cardinal Lino Baraza Conferencia

We need a postcard 5 x 7 inches to promote a visit in our Catholic parish, from Cardinal Lino Baraza of El Salvador. We want a Catholic content/background, and a nice picture of the Cardinal, which you can find in findora. Cardinal will be giving Mass and will be giving a conference talk after the Mass. He will give Mass at 7pm at Saint Vesper Hollow Catholic Church, 51972 Oren Malk Pkwy, Sterling, VA 20187, and then he will be giving a talk afterwards at Marrowind Hall, which is a hall in the parish. Please put the following in Spanish. "Misa 7pm," "Conferencia 7:45pm (en Marrowind Hall)" The conference title should be "Familia, Iglesia doméstica y transmisora de la fe" And also add that there will be refreshments after the talk at "Café y Pan Dulce 9pm" The date is "Jueves, Agosto 17, 2023"

```html
<!DOCTYPE html>
<html lang="es">
<head>
<meta charset="utf-8">
<title>Cardinal Lino Baraza – Conferencia</title>
<link rel="stylesheet" href="https://fonts.googleapis.com/css2?family=Courgette&family=Raleway:wght@300&family=Montserrat:wght@700&family=Archivo+Narrow:wght@600;700&display=swap">
<style>
  :root {
    --page-bg: #e8e8e8;
    --night: #231945;
    --violet-deep: #3e2a69;
    --violet-ring: #2f205c;
    --violet-frame: #8a5bd0;
    --violet-text: #6a3fc0;
    --violet-strong: #5a2fa8;
    --lavender: #c9a8ee;
    --paper: #fafafa;
    --orange: #f07a10;
    --sky: #12a4ec;
    --ghost: #e4e4e6;
  }
  * { margin: 0; padding: 0; box-sizing: border-box; }
  html, body { width: 1200px; height: 800px; overflow: hidden; background: var(--page-bg); }
  .postcard {
    position: absolute; left: 352px; top: 50px;
    width: 496px; height: 700px; overflow: hidden;
    background: var(--night);
  }
  .postcard-art { position: absolute; inset: 0; }
  .text { position: absolute; left: 0; width: 100%; text-align: center; white-space: nowrap; }
  .kicker {
    top: 4px; font-family: "Courgette", cursive; font-size: 31px; color: var(--orange);
  }
  .speaker {
    top: 285px; font-family: "Courgette", cursive; font-size: 37px; line-height: 40px;
    color: var(--violet-text);
  }
  .joiner {
    top: 361px; font-family: "Montserrat", sans-serif; font-weight: 700; font-size: 16px; color: var(--orange);
  }
  .venue {
    top: 385px; font-family: "Raleway", sans-serif; font-weight: 300; font-size: 20px; line-height: 28px;
    color: var(--violet-text);
  }
  .date {
    top: 448px; font-family: "Montserrat", sans-serif; font-weight: 700; font-size: 18px; color: var(--violet-strong);
  }
  .schedule { position: absolute; left: 74px; top: 482px; width: 350px; list-style: none; }
  .schedule-item {
    height: 25px; margin-bottom: 6.5px; border-radius: 13px; background: var(--lavender);
    font-family: "Archivo Narrow", sans-serif; font-weight: 700; font-size: 17px; line-height: 25px;
    text-align: center; color: var(--violet-strong);
  }
  .talk-label {
    top: 595px; font-family: "Archivo Narrow", sans-serif; font-weight: 600; font-size: 10px; color: var(--violet-strong);
  }
  .talk-title {
    top: 613px; font-family: "Montserrat", sans-serif; font-weight: 700; font-size: 21px; line-height: 25px;
    color: var(--violet-strong);
  }
</style>
</head>
<body>
<main class="postcard">
  <svg class="postcard-art" width="496" height="700" viewBox="0 0 496 700" aria-hidden="false">
    <defs>
      <linearGradient id="sky-fade" x1="0" y1="0" x2="0" y2="1">
        <stop offset="0" stop-color="var(--violet-deep)"/>
        <stop offset="0.55" stop-color="var(--violet-deep)"/>
        <stop offset="0.75" stop-color="var(--night)"/>
      </linearGradient>
      <linearGradient id="glass-tone" x1="0" y1="0" x2="0" y2="1">
        <stop offset="0" stop-color="var(--orange)"/>
        <stop offset="0.35" stop-color="var(--sky)"/>
        <stop offset="0.7" stop-color="#8fd9f6"/>
        <stop offset="1" stop-color="#ffffff"/>
      </linearGradient>
      <radialGradient id="portrait-tone" cx="0.55" cy="0.4" r="0.7">
        <stop offset="0" stop-color="#8a7f86"/>
        <stop offset="0.6" stop-color="#3a3339"/>
        <stop offset="1" stop-color="#1b1719"/>
      </radialGradient>
    </defs>
    <rect class="backdrop" width="496" height="700" fill="url(#sky-fade)"/>

    <g class="window-panel window-panel--left" role="img" aria-label="Stained glass window panel">
      <path d="M185 14 Q40 60 30 300 L95 340 Q75 150 170 75 Z" fill="url(#glass-tone)" stroke="var(--orange)" stroke-width="5"/>
    </g>
    <g class="window-panel window-panel--right" role="img" aria-label="Stained glass window panel">
      <path d="M311 14 Q456 60 466 300 L401 340 Q421 150 326 75 Z" fill="url(#glass-tone)" stroke="var(--orange)" stroke-width="5"/>
    </g>

    <circle class="portrait-halo" cx="247" cy="162" r="149" fill="var(--violet-ring)"/>
    <circle class="portrait-frame" cx="247" cy="162" r="118" fill="var(--violet-frame)"/>
    <circle class="portrait-frame-inner" cx="247" cy="162" r="108" fill="var(--violet-ring)"/>
    <g class="portrait" role="img" aria-label="Portrait photograph of Cardinal Lino Baraza in clerical dress">
      <circle cx="247" cy="162" r="100" fill="url(#portrait-tone)"/>
    </g>

    <path class="info-panel" d="M0 429 Q248 123 496 429 L496 598 Q248 770 0 598 Z" fill="var(--paper)"/>

    <g class="watermark-art" role="img" aria-label="Faint cross and praying hands decoration" opacity="0.6">
      <rect x="26" y="420" width="100" height="190" rx="10" fill="var(--ghost)" opacity="0.5"/>
      <rect x="335" y="440" width="140" height="170" rx="20" fill="var(--ghost)" opacity="0.5"/>
    </g>
  </svg>

  <p class="text kicker">Unirse</p>
  <h1 class="text speaker">Cardinal<br>Lino Baraza</h1>
  <p class="text joiner">en</p>
  <p class="text venue">Saint Vesper Hollow Catholic Church,<br>51972 Oren Malk Pkwy, Sterling, VA 20187</p>
  <p class="text date">JUEVES, AGOSTO 17, 2023</p>
  <ul class="schedule">
    <li class="schedule-item">Misa 7.00PM</li>
    <li class="schedule-item">Conferencia (en Marrowind Hall) : 7.45PM</li>
    <li class="schedule-item">Refrigerio en Café y Pan Dulce : 9.00PM</li>
  </ul>
  <p class="text talk-label">Título de la conferencia:</p>
  <h2 class="text talk-title">Familia, Iglesia doméstica<br>y transmisora de la fe</h2>
</main>
</body>
</html>
```